Wren's Velvet Lantern Soiree

We need an invitation that compliments a start studded guest list of the most influential 20-30 year olds in manhattan. The theme of the party is moroccan nights with black and gold color scheme. 9pm - all night, cocktails and horderves followed by Dj Pollux and surprise entertainment. Attire gypsy chic. Address will be provided upon RSVP

Font styles to use
Decorative
Script

Colors
fbed22
000000

Requirements
Should not have
• basic

```html
<!DOCTYPE html>
<html lang="en">
<head>
<meta charset="utf-8">
<title>Wren's Velvet Lantern Soiree – Invitation</title>
<link rel="stylesheet" href="https://fonts.googleapis.com/css2?family=Yanone+Kaffeesatz:wght@400;500;700&display=swap">
<style>
  :root {
    --backdrop: #2b2622;
    --card: #221d19;
    --gold: #e2b451;
    --gold-deep: #b98a34;
  }
  * { margin: 0; padding: 0; box-sizing: border-box; }
  html, body {
    width: 1200px;
    height: 813px;
    overflow: hidden;
    background: var(--backdrop);
  }
  .invitation {
    position: absolute;
    left: 390px;
    top: 36px;
    width: 420px;
    height: 740px;
    background: var(--card);
    color: var(--gold);
    font-family: "Yanone Kaffeesatz", "Arial Narrow", sans-serif;
    text-transform: uppercase;
    text-align: center;
    display: flex;
    flex-direction: column;
    align-items: center;
    padding-top: 70px;
  }
  .invitation__ornament {
    width: 200px;
    height: 200px;
    display: block;
  }
  .invitation__title {
    margin-top: 46px;
    font-size: 38px;
    font-weight: 500;
    letter-spacing: 0.5px;
  }
  .invitation__rule {
    width: 250px;
    height: 2px;
    background: var(--gold);
    margin: 12px 0;
  }
  .invitation__time {
    font-size: 48px;
    font-weight: 700;
    line-height: 1;
    letter-spacing: 1px;
  }
  .invitation__details {
    margin-top: 26px;
    font-size: 25px;
    font-weight: 400;
    line-height: 1.22;
    letter-spacing: 0.5px;
  }
  .invitation__note {
    margin-top: 24px;
    font-size: 15px;
    font-weight: 400;
    letter-spacing: 0.5px;
  }
</style>
</head>
<body>
  <article class="invitation">
    <svg class="invitation__ornament" viewBox="0 0 200 200" role="img" aria-label="Gold Moroccan geometric tile ornament">
      <defs>
        <radialGradient id="ornament-tone" cx="50%" cy="50%" r="60%">
          <stop offset="0%" stop-color="#e2b451" stop-opacity="0.55"/>
          <stop offset="100%" stop-color="#b98a34" stop-opacity="0.25"/>
        </radialGradient>
      </defs>
      <rect x="0" y="0" width="200" height="200" fill="url(#ornament-tone)"/>
    </svg>

    <h1 class="invitation__title">Moroccan Nights</h1>
    <div class="invitation__rule"></div>
    <p class="invitation__time">9PM - All Night</p>
    <div class="invitation__rule"></div>

    <p class="invitation__details">
      Cocktails and horderves<br>
      followed by Dj Pollux and<br>
      surprise entertainment<br>
      attire required gypsy chic
    </p>

    <p class="invitation__note">Adress will be provided upon RSVP</p>
  </article>
</body>
</html>
```